Double-sided business card needed - specific brief

We need a double sided business card designed for our company Radiant Trimline. Having lost a lot of weight myself, the back of the card needs to show my before and after pictures. It needs to cover the entire back side of the card. This might be with my two before pictures over set on top of my main after picture or in separate frames. I'll leave that to your artistic consideration. The front needs to have our logo with contact details centred below.

The cards will be printed by PRINTVEX.com and will be rectangular, 84mm x 55mm, but with ROUNDED edges. Please therefore present your designs rectangular but with rounded edges if possible.

The card should be designed in LANDSCAPE orientation.

As well as the logo, the front of the card should have the following details:

Carol Whitby
Weight Loss Motivator with 189lb personal loss
carol@radiant-trimline.example
+44 (0)7700 900418

The website is important so should perhaps be more bold than the rest:
www.radiant-trimline.example

My brand colours are: Pink #CD2366, Light Pink #FD88AD. Blue #1C9CB1, Light Blue #64C4DE

Target Market(s)

Women 30+

Contact Information for Business Card

As description above

Font styles to use
Sans Serif

Requirements
Must have
• Double sided.
• Back side entirely covered with my before and after pictures.
• You may wish to float my before pictures on top of my after picture or add them in different frames. I look forward to seeing your different suggestions.

```html
<!DOCTYPE html>
<html lang="en">
<head>
<meta charset="utf-8">
<title>Radiant Trimline – Business Card</title>
<link rel="stylesheet" href="https://fonts.googleapis.com/css2?family=EB+Garamond:wght@400;500;600&display=swap">
<style>
  :root {
    --pink: #cd2366;
    --pink-bright: #e04a8c;
    --light-pink: #fd88ad;
    --blue: #1c9cb1;
    --light-blue: #64c4de;
    --ink: #2a2a2a;
    --paper: #ffffff;
    --paper-shade: #ececec;
    --backdrop: #2b2b2b;
  }
  * { margin: 0; padding: 0; box-sizing: border-box; }
  html, body {
    width: 1200px; height: 997px; overflow: hidden;
    background: var(--backdrop);
    font-family: "EB Garamond", Georgia, serif;
  }
  .canvas {
    position: relative; width: 1200px; height: 997px;
    display: flex; flex-direction: column; align-items: center; justify-content: center; gap: 36px;
  }
  .card {
    position: relative; width: 660px; height: 432px;
    border-radius: 18px; overflow: hidden;
  }

  /* ---------- Back side ---------- */
  .card-back { background: linear-gradient(135deg, var(--pink-bright), var(--pink)); }
  .after-photo {
    position: absolute; inset: 0;
    clip-path: polygon(0 0, 100% 0, 100% 90%, 36% 90%, 36% 40%, 0 40%);
    background: linear-gradient(120deg, #d9cdb4 0%, #a89a80 35%, #5a4a3c 65%, #2a3560 100%);
  }
  .photo-tag {
    position: absolute; padding: 3px 12px;
    background: var(--light-pink); color: var(--paper);
    font-size: 17px; letter-spacing: 0.5px;
    border-radius: 4px 14px 4px 4px;
  }
  .tag-before { left: 268px; top: 118px; }
  .tag-after { left: 428px; top: 162px; }
  .before-frame {
    position: absolute; border: 4px solid var(--light-blue);
    border-radius: 16px; overflow: hidden;
    box-shadow: 0 3px 10px rgba(0,0,0,0.35);
  }
  .before-1 {
    left: 34px; top: 148px; width: 280px; height: 200px;
    background: linear-gradient(160deg, #e8e2dc, #b98a74 55%, #6a4a3a);
  }
  .before-2 {
    left: 180px; top: 232px; width: 320px; height: 186px;
    background: linear-gradient(150deg, #7a8a5a, #e6e4e0 50%, #3a3030);
  }

  /* ---------- Front side ---------- */
  .card-front {
    background: linear-gradient(160deg, var(--paper) 40%, var(--paper-shade));
    color: var(--ink);
  }
  .holder { position: absolute; left: 172px; top: 40px; }
  .holder-name {
    color: var(--blue); font-size: 22px; font-weight: 500;
    letter-spacing: 1.5px; text-transform: uppercase;
  }
  .holder-role { font-size: 16px; margin-top: 2px; }
  .brand-name {
    position: absolute; left: 0; right: 0; top: 168px;
    text-align: center; color: var(--pink);
    font-size: 38px; font-weight: 500; letter-spacing: 1px; text-transform: uppercase;
  }
  .contacts {
    position: absolute; left: 0; right: 0; top: 290px;
    display: flex; justify-content: center; gap: 48px;
    font-size: 18px;
  }
  .contact { display: flex; align-items: center; gap: 10px; }
  .contact-icon { width: 26px; height: 26px; }
  .web-band {
    position: absolute; left: 0; right: 0; bottom: 0; height: 70px;
    background: linear-gradient(90deg, var(--pink-bright), var(--pink));
    display: flex; align-items: center; justify-content: center;
    color: var(--paper); font-size: 19px; font-weight: 600; letter-spacing: 5px;
  }
</style>
</head>
<body>
<main class="canvas">

  <section class="card card-back" aria-label="Card back">
    <div class="after-photo" role="img" aria-label="After photo: Carol seated on a leather sofa in a bright room"></div>
    <span class="photo-tag tag-before">Before</span>
    <span class="photo-tag tag-after">After</span>
    <div class="before-frame before-1" role="img" aria-label="Before photo: Carol in a wedding veil"></div>
    <div class="before-frame before-2" role="img" aria-label="Before photo: Carol holding a cat in a garden"></div>
  </section>

  <section class="card card-front" aria-label="Card front">
    <div class="holder">
      <p class="holder-name">Carol Whitby</p>
      <p class="holder-role">Weight Loss Motivator with 189lb personal loss</p>
    </div>

    <p class="brand-name">Radiant Trimline</p>

    <div class="contacts">
      <p class="contact">
        <svg class="contact-icon" viewBox="0 0 26 26" aria-hidden="true">
          <circle cx="13" cy="13" r="13" fill="var(--pink)"/>
          <path d="M8 9c0-1 1-2 2-2h6c1 0 2 1 2 2v1h-3V9h-4v1H8z M9 12h8l1 6H8z" fill="#fff"/>
        </svg>
        <span>+44 (0)7700 900418</span>
      </p>
      <p class="contact">
        <svg class="contact-icon" viewBox="0 0 26 26" aria-hidden="true">
          <circle cx="13" cy="13" r="13" fill="var(--pink)"/>
          <rect x="7" y="8.5" width="12" height="9" fill="#fff"/>
          <path d="M7 8.5l6 5 6-5" fill="none" stroke="var(--pink)" stroke-width="1.3"/>
        </svg>
        <span>carol@radiant-trimline.example</span>
      </p>
    </div>

    <div class="web-band">www.radiant-trimline.example</div>
  </section>

</main>
</body>
</html>
```